Lumetta small bites needs a website.

I have a small dessert bite catering business creating uniquely crafted small dessert bites made with high quality ingredients focusing on gluten free and vegan options.
I would like a website to show off my creations and provide a way for customers to reach me. I work out of a catering kitchen so would include the address of the kitchen as well as my phone number and email etc.

I already own the “www.lumettasmallbites.example” domain but have not used it yet. I have zero knowledge on website creation and design so need help in design as well as coding. I’m not sure how many pages I need designed. I would like one for the dessert bar / catering focus and one for my tasting boxes. I would like a way to upload new tasting box pictures and information to the website as they come out.

Target Market(s)

Individuals or businesses wanting to buy small bite desserts for weddings, gatherings and events for a dessert bar table. I also am creating monthly / seasonal tasting boxes (holiday, Valentine’s Day, etc) that I’d like to highlight.

Industry/Entity Type

Dessert catering, vegan and gluten free

Coding

Coded - Design and coding required

Number of Pages Required

2 page

Colors
E54698
E96AAD
F1A4CE
F9D9EA
FCEFF6

Requirements
Must have
• Pictures of my desserts and text explaining my process of creating individual flavor profiled desserts for people. I would like it to match the current color scheme and vibe of my logo. Must say that I am a catering company so don’t have a bakery but do have frozen tasting boxes available at the store front of the commercial kitchen that I use.
Nice to have
• I would like the website to have the vibe and colors of my logo but would welcome additional creativity from the designer. Include pink and brown as the main colors

```html
<!DOCTYPE html>
<html lang="en">
<head>
<meta charset="utf-8">
<title>Lumetta Small Bites</title>
<link href="https://fonts.googleapis.com/css2?family=Playfair+Display:wght@600;700&family=Poppins:wght@400;500;600&display=swap" rel="stylesheet">
<style>
  :root {
    --pink-strong: #e54698;
    --pink-mid: #e96aad;
    --pink-soft: #f1a4ce;
    --pink-pale: #f9d9ea;
    --pink-mist: #fcf0f6;
    --brown: #5a3a2e;
    --brown-text: #4a3129;
    --white: #ffffff;
    --photo-top: #d9c89a;
    --photo-mid: #f0e4d4;
    --photo-low: #dcb08c;
    --photo-base: #b87462;
  }
  * { box-sizing: border-box; margin: 0; padding: 0; }
  html, body { width: 682px; height: 1200px; overflow: hidden; }
  body {
    font-family: "Poppins", sans-serif;
    color: var(--brown-text);
    background: var(--pink-mist);
  }
  .page { width: 682px; height: 1200px; position: relative; }

  .site-header {
    height: 32px;
    background: var(--pink-mist);
    display: flex;
    justify-content: flex-end;
    align-items: center;
    padding-right: 11px;
    position: relative;
    z-index: 2;
  }
  .brand {
    position: absolute;
    left: 9px; top: 0;
    width: 62px; height: 57px;
    background: var(--pink-mist);
    border-radius: 0 0 5px 5px;
    display: flex; flex-direction: column;
    align-items: center; justify-content: center; gap: 4px;
  }
  .brand-dot {
    width: 22px; height: 22px; border-radius: 50%;
    border: 1.5px solid var(--brown);
  }
  .brand-name {
    font-family: "Poppins", sans-serif;
    font-weight: 600; font-size: 9px;
    color: var(--brown);
  }
  .main-nav { display: flex; gap: 8px; }
  .main-nav a {
    font-size: 5.6px; color: var(--brown); text-decoration: none; font-weight: 500;
  }

  .hero {
    height: 143px;
    background: linear-gradient(90deg, #efa3cf 0%, #f4c2dd 55%, #f8d4e7 100%);
    text-align: center;
    padding-top: 36px;
  }
  .hero-title {
    font-family: "Playfair Display", serif; font-weight: 700;
    font-size: 17px; color: var(--brown);
  }
  .hero-lede {
    font-size: 6.6px; line-height: 11px; margin-top: 11px; color: var(--brown-text);
  }
  .btn {
    display: inline-block;
    border-radius: 9px;
    font-size: 5.4px; font-weight: 600;
    color: var(--white);
    text-decoration: none;
    height: 16px; line-height: 16px;
  }
  .btn-pink { background: var(--pink-strong); padding: 0 10px; }
  .btn-brown { background: var(--brown); padding: 0 10px; }
  .hero .btn { margin-top: 11px; }

  .about {
    height: 628px;
    padding: 24px 134px 0;
  }
  .section-title {
    font-family: "Playfair Display", serif; font-weight: 700;
    font-size: 14px; color: var(--brown);
  }
  .about p {
    font-size: 5.1px; line-height: 8.2px; margin-top: 6px; color: var(--brown-text);
  }
  .about .section-title { margin-bottom: 4px; }
  .about .btn { margin-top: 5px; }
  .about-photo {
    margin-top: 10px;
    width: 414px; height: 476px;
    border-radius: 3px;
    background: linear-gradient(180deg, var(--photo-top) 0%, var(--photo-mid) 42%, var(--photo-low) 72%, var(--photo-base) 100%);
    box-shadow: 0 1px 4px rgba(90, 58, 46, 0.15);
  }

  .gallery {
    height: 221px;
    background: var(--pink-pale);
    text-align: center;
    padding-top: 23px;
  }
  .gallery-grid {
    display: flex; gap: 5px; margin-top: 10px; height: 119px;
  }
  .gallery-tile { flex: 1; }
  .tile-cannoli { background: linear-gradient(180deg, #c9c6a8, #ece6df 55%, #cfaea4); }
  .tile-cheesecake { background: linear-gradient(180deg, #c2c0ba, #f0ecdc 55%, #e2d8b8); }
  .tile-opera { background: linear-gradient(180deg, #c6c3bd, #ece9e4 50%, #a88a84); }
  .tile-table { background: linear-gradient(180deg, #8b7468, #a7775a 55%, #b98358); }
  .gallery .btn { margin-top: 11px; }

  .contact {
    height: 158px;
    text-align: center;
    padding-top: 22px;
  }
  .contact-intro {
    font-size: 5.3px; line-height: 8.2px; margin-top: 6px;
  }
  .contact-list { margin-top: 9px; font-size: 5.3px; line-height: 8.5px; }
  .contact-list dt { font-weight: 600; display: inline; }
  .contact-list dd { display: inline; }
  .contact-list a { color: var(--pink-strong); text-decoration: none; font-weight: 500; }
  .contact-row { margin-bottom: 3.5px; }
  .contact-row.address dt { display: block; }
  .contact-row.address dd { display: block; }

  .site-footer {
    height: 18px; background: var(--brown);
    color: var(--pink-mist);
    font-size: 4.6px; text-align: center; line-height: 18px;
  }
</style>
</head>
<body>
<div class="page">
  <header class="site-header">
    <div class="brand">
      <span class="brand-dot"></span>
      <span class="brand-name">Lumetta</span>
    </div>
    <nav class="main-nav">
      <a href="#">Home</a>
      <a href="#">Dessert Bar &amp; Catering</a>
      <a href="#">Tasting Boxes</a>
      <a href="#">Contact</a>
    </nav>
  </header>

  <section class="hero">
    <h1 class="hero-title">Uniquely Flavorful Bites</h1>
    <p class="hero-lede">Artisanal vegan &amp; gluten-free dessert bites crafted for your<br>celebrations and everyday indulgence.</p>
    <a class="btn btn-pink" href="#">Explore Tasting Boxes</a>
  </section>

  <section class="about">
    <h2 class="section-title">About Lumetta</h2>
    <p>Lumetta Small Bites is a boutique dessert catering company rooted in the belief that every celebration deserves food that delights all the senses. Our founder specializes in crafting miniature treats that combine global flavors with modern technique, using premium ingredients and offering vegan and gluten-free options so everyone can enjoy.</p>
    <p>From weddings and corporate receptions to intimate dinners, Lumetta’s signature bites are designed to be beautiful, flavorful and memorable. We work closely with each client to understand their palette and create bespoke menus that reflect their story.</p>
    <a class="btn btn-brown" href="#">Our Process</a>
    <div class="about-photo" role="img" aria-label="Plate of three dessert bites on a striped table runner with a vase of yellow roses and purple flowers"></div>
  </section>

  <section class="gallery">
    <h2 class="section-title">Taste the Inspiration</h2>
    <div class="gallery-grid">
      <div class="gallery-tile tile-cannoli" role="img" aria-label="Platter of mini cannoli and cherry-topped cheesecake bites"></div>
      <div class="gallery-tile tile-cheesecake" role="img" aria-label="Tray of lemon ginger cheesecake bites with a chalkboard label"></div>
      <div class="gallery-tile tile-opera" role="img" aria-label="Stand of raspberry opera cake squares with a chalkboard label"></div>
      <div class="gallery-tile tile-table" role="img" aria-label="Dessert bar table set with trays of assorted small bites"></div>
    </div>
    <a class="btn btn-pink" href="#">View Full Gallery</a>
  </section>

  <section class="contact">
    <h2 class="section-title">Get In Touch</h2>
    <p class="contact-intro">Ready to create the dessert bar of your dreams or order a tasting box? Reach out and<br>let’s talk about your event and your unique flavor inspirations.</p>
    <dl class="contact-list">
      <div class="contact-row"><dt>Email:</dt> <dd><a href="#">info@lumettasmallbites.example</a></dd></div>
      <div class="contact-row"><dt>Phone:</dt> <dd><a href="#">+92 300-555-0142</a></dd></div>
      <div class="contact-row address"><dt>Kitchen Address:</dt><dd>Commercial Kitchen</dd><dd>Lahore, Punjab, Pakistan</dd></div>
    </dl>
  </section>

  <footer class="site-footer">© 2026 Lumetta Small Bites. All rights reserved.</footer>
</div>
</body>
</html>
```